Business Card Design and Stationary design for consulting firm

Harbourline Sourcing are looking for a new business card design and a design for their A4 letterhead / A4 invoices.

We are seeking to heavily increase our brand awareness and require a business card that's professional in appearance but also shows flare and innovation. A card design that people will remember.

About Us
Harbourline Sourcing are `The Sourcing Crew’.
Our mission is to be one of Australia’s greatest companies. Our aim is to help our customers achieve the best result from their purchasing experience.

Our Requirement:
• IMPACT! IMPACT! IMPACT!
• BUSINESS & PROFESSIONAL LOOKING

• Our business colours are orange, blue and green (See the logo attached).

We have provided an Art Design specification (attached) that needs to be followed for you to win the design. This also has the font, which is used on the logo.

We are after a two sided business card

Side One should have the:
The company Logo
The Sourcing Crew
www.harbourlinesourcing.com.au
Procure | Personnel | Probity & Privacy
Sydney | Melbourne | Adelaide | Brisbane

Side Two
Logo (optional)
Harbourline Sourcing (optional)
Employee details (details listed below)

The above format is our preferred option, but if you think you can come up with something better, feel free to put it forward.

We are leaving the design up to you, but it must incorporate the logo.

We will need a template that we can change the employee details on, as we will be adding more staff over the coming months.

The details below are for one employee per card with the same design.
------------------------

Employee Details:

Marcus Oldfield MBA, MMgmtStratProc
Principal Consultant
0412 356 917
Marcus@harbourlinesourcing.com.au

Brianna Tolhurst
Consulting Manager
0431 629 084
Brianna@harbourlinesourcing.com.au

Our website is www.harbourlinesourcing.com.au

The Letterhead / invoice needs to incorporate:
the company Logo
The Sourcing Crew
Sydney | Melbourne | Adelaide | Brisbane but otherwise the design is over to you.

This file needs to be delivered in word format as other detail will be added to the documents.

We look forward to you award winning designs. If you require any further information please feel free to contact us.

Regards
Harbourline Sourcing

Target Market(s)

Our Target market is companies with 80+ employees. The market we segment is heavily male based, between the ages of 35-55 years of age.

Industry/Entity Type

Consulting

Contact Information for Business Card

See Project Description

Font styles to use
Other font styles liked:
• See Art Specification

Requirements
Must have
• Company Colours, See Project Description
Should not have
• Be outside the Art specification guidelines

```html
<!DOCTYPE html>
<html lang="en">
<head>
<meta charset="utf-8">
<title>Harbourline Sourcing – Business Card</title>
<link href="https://fonts.googleapis.com/css2?family=Open+Sans:wght@400;600;700&display=swap" rel="stylesheet">
<style>
  :root {
    --page: #e9e6e1;
    --card: #141414;
    --card-edge: #1d1d1d;
    --map-a: #25303a;
    --map-b: #141414;
    --band-a: #1597cf;
    --band-b: #3cc6f0;
    --white: #ffffff;
    --muted: #c9c9c9;
    --orange: #f6a01a;
    --green: #5cc23a;
    --blue: #2a9fe0;
  }
  * { margin: 0; padding: 0; box-sizing: border-box; }
  html, body { width: 821px; height: 1200px; overflow: hidden; }
  body {
    background: var(--page);
    font-family: "Open Sans", Arial, sans-serif;
    position: relative;
  }
  .card {
    position: absolute;
    left: 60px;
    width: 700px;
    height: 400px;
    background: var(--card);
    border-radius: 4px;
    overflow: hidden;
    box-shadow: 0 10px 28px rgba(0,0,0,.25);
  }
  .card--details { top: 150px; }
  .card--front { top: 650px; }
  .world-map {
    position: absolute;
    left: 150px; top: 30px;
    width: 520px; height: 290px;
    background: radial-gradient(ellipse at 50% 50%, var(--map-a) 0%, var(--map-b) 70%);
    opacity: .85;
  }
  .band {
    position: absolute;
    left: 0; right: 0; bottom: 0;
    height: 58px;
    background: linear-gradient(90deg, var(--band-a), var(--band-b));
    display: flex; align-items: center;
    color: var(--white);
  }
  .brand {
    position: absolute;
    display: flex; align-items: center; gap: 12px;
    color: var(--white);
    font-weight: 700;
    letter-spacing: .06em;
    text-transform: uppercase;
  }
  .brand__dot {
    width: 30px; height: 30px; border-radius: 50%;
    background: var(--orange);
    flex: none;
  }
  .card--details .brand { left: 50px; top: 210px; font-size: 22px; }
  .divider { position: absolute; left: 0; top: 0; }
  .person { position: absolute; left: 400px; top: 64px; }
  .person__name { color: var(--orange); font-size: 20px; font-weight: 600; }
  .person__role { color: var(--muted); font-size: 14px; margin-top: 2px; }
  .contact { list-style: none; margin-top: 30px; }
  .contact li {
    display: flex; align-items: center; gap: 10px;
    color: var(--white); font-size: 14px; margin-bottom: 12px;
  }
  .contact svg { flex: none; }
  .band--web { justify-content: flex-end; padding-right: 40px; font-size: 15px; }
  .card--front .brand { left: 120px; top: 120px; font-size: 32px; }
  .services {
    position: absolute; left: 120px; top: 200px;
    color: var(--white); font-size: 15px; line-height: 1.6;
  }
  .band--tagline {
    justify-content: flex-start; padding-left: 120px;
    font-size: 17px; font-weight: 600; letter-spacing: .32em;
    text-transform: uppercase;
  }
</style>
</head>
<body>

<section class="card card--details">
  <div class="world-map" role="img" aria-label="Faint dotted world map in dark blue-grey"></div>
  <svg class="divider" width="700" height="400" aria-hidden="true">
    <line x1="150" y1="180" x2="370" y2="130" stroke="#ffffff" stroke-width="2" stroke-linecap="round" opacity=".75"/>
  </svg>
  <div class="brand"><span class="brand__dot"></span>Harbourline Sourcing</div>
  <div class="person">
    <p class="person__name">Brianna Tolhurst</p>
    <p class="person__role">Consulting Manager</p>
    <ul class="contact">
      <li>
        <svg width="22" height="22" viewBox="0 0 22 22" aria-hidden="true">
          <circle cx="11" cy="11" r="11" fill="var(--green)"/>
          <path d="M7.5 6.5c.6-.6 1.4-.4 1.7.3l.7 1.5c.2.5 0 1-.4 1.3l-.6.4c.6 1.3 1.6 2.3 2.9 2.9l.4-.6c.3-.4.8-.6 1.3-.4l1.5.7c.7.3.9 1.1.3 1.7l-.7.7c-.6.6-1.6.7-2.5.3-2.3-1-4.1-2.8-5.1-5.1-.4-.9-.3-1.9.3-2.5z" fill="#fff"/>
        </svg>
        0431 629 084
      </li>
      <li>
        <svg width="22" height="22" viewBox="0 0 22 22" aria-hidden="true">
          <rect width="22" height="22" rx="4" fill="var(--blue)"/>
          <rect x="5" y="7" width="12" height="8" rx="1" fill="none" stroke="#fff" stroke-width="1.4"/>
          <path d="M5.5 7.5L11 11.5l5.5-4" fill="none" stroke="#fff" stroke-width="1.4"/>
        </svg>
        Brianna@harbourlinesourcing.com.au
      </li>
    </ul>
  </div>
  <div class="band band--web">www.harbourlinesourcing.com.au</div>
</section>

<section class="card card--front">
  <div class="world-map" role="img" aria-label="Faint dotted world map in dark blue-grey"></div>
  <div class="brand"><span class="brand__dot"></span>Harbourline Sourcing</div>
  <div class="services">
    <p>Procure | Personnel | Probity &amp; Privacy</p>
    <p>Sydney | Melbourne | Adelaide | Brisbane</p>
  </div>
  <div class="band band--tagline">The Sourcing Crew</div>
</section>

</body>
</html>
```